Postcard for Current Clients

We need a postcard to offer a 25% discount for Annual Inspections to current clients that refer us to new clients.
Attached is some info regarding our services
We want to obtain new clients by offering current clients a discounted rate
Our industry is unique and our target market for this project is specific to Property Managers and Building Engineers.

Target Market(s)

Current Clients - Property Managers & Building Engineers

Industry/Entity Type

Window Cleaning

Requirements
Must have
• Red/White/Blue

```html
<!DOCTYPE html>
<html lang="en">
<head>
<meta charset="utf-8">
<title>Harlow Safety – Referral Postcard</title>
<link href="https://fonts.googleapis.com/css2?family=Roboto+Condensed:wght@400;700&family=Tinos:ital,wght@0,400;0,700;1,400&display=swap" rel="stylesheet">
<style>
:root{
  --navy:#3a3a92;
  --red:#e32b33;
  --deep-red:#8e1d22;
  --sky:#2f9ad8;
  --ink:#2d2d2d;
  --white:#ffffff;
  --page:#ffffff;
  --frame:#3a3a92;
}
*{margin:0;padding:0;box-sizing:border-box}
html,body{width:902px;height:1200px;overflow:hidden;background:var(--page)}
body{position:relative;font-family:"Tinos",serif;color:var(--white)}
.abs{position:absolute}

/* ---------- Front ---------- */
.front{left:38px;top:32px;width:824px;height:548px;border:1px solid #cfcfcf;background:var(--white)}
.brand{left:14px;top:10px;display:flex;align-items:center;gap:6px;font-family:"Tinos",serif;font-style:italic;font-weight:700;font-size:17px;color:var(--red)}
.brand .dot{width:10px;height:10px;border-radius:50%;background:var(--navy)}
.front-contact{right:194px;top:26px;text-align:right;font-family:"Tinos",serif;font-weight:700;font-size:11.5px;line-height:14px;color:var(--ink)}
.front-banner{left:42px;top:84px;width:588px;height:24px}
.front-banner span{position:absolute;left:0;right:0;top:2px;text-align:center;font-family:"Roboto Condensed",sans-serif;font-weight:700;font-size:17px;color:var(--white);white-space:nowrap}
.letter{left:0;top:106px;width:646px;height:394px;background:var(--navy);padding:14px 14px 0 37px;font-size:10.6px;line-height:12px;text-align:justify}
.letter p{margin-bottom:3px}
.letter .salute{font-style:italic}
.letter ul{list-style:none;margin-bottom:2px}
.letter li{padding-left:16px;position:relative;margin-bottom:4px}
.letter li::before{content:"";position:absolute;left:1px;top:2px;border-left:7px solid var(--white);border-top:4px solid transparent;border-bottom:4px solid transparent}
.letter li::after{content:"";position:absolute;left:2.5px;top:4px;border-left:4px solid var(--navy);border-top:2px solid transparent;border-bottom:2px solid transparent}
.letter h3{font-size:11px;font-weight:700;margin-bottom:1px}
.front-photo{left:646px;top:0;width:178px;height:500px;background:linear-gradient(180deg,#7a8ba3 0%,#9fb0c4 30%,#8c8a84 70%,#6e6a62 100%)}
.cta-bar{left:0;top:500px;width:824px;height:48px}
.cta-bar .cta-text{position:absolute;left:62px;top:10px;font-family:"Roboto Condensed",sans-serif;font-weight:700;font-size:25px;color:var(--navy);white-space:nowrap}
.cta-bar .cta-phone{position:absolute;left:500px;top:6px;font-family:"Roboto Condensed",sans-serif;font-weight:700;font-size:34px;color:var(--white);white-space:nowrap}

.seal{width:94px;height:94px}
.seal .pct{position:absolute;left:0;right:0;top:10px;text-align:center;font-family:"Tinos",serif;font-weight:700;font-size:40px;line-height:40px;color:var(--white)}
.seal .pct small{font-size:24px}
.seal .word{position:absolute;left:0;right:0;top:54px;text-align:center;font-family:"Tinos",serif;font-weight:700;font-size:18px;color:var(--white)}

/* ---------- Back ---------- */
.back{left:38px;top:609px;width:824px;height:549px;background:var(--white);border:1px solid #cfcfcf}
.back-panel{left:0;top:0;width:588px;height:419px;background:var(--navy)}
.back-brand{left:40px;top:40px;width:160px;display:flex;align-items:flex-start;gap:8px;font-family:"Tinos",serif;font-style:italic;font-weight:700;font-size:30px;line-height:34px;color:var(--white)}
.back-brand .dot{flex:none;width:14px;height:14px;margin-top:11px;border-radius:50%;background:var(--red)}
.audience{left:182px;top:12px;width:330px;text-align:center;font-family:"Roboto Condensed",sans-serif;font-weight:700;font-size:14px;color:var(--white);white-space:nowrap}
.photo{width:158px;border:1px solid #c9c9d8}
.back-address{left:24px;top:441px;font-family:"Roboto Condensed",sans-serif;font-size:13px;color:var(--ink);white-space:nowrap}
.back-cta{left:0;top:459px;width:588px;height:34px;background:var(--red)}
.back-cta .cta-text{position:absolute;left:24px;top:6px;font-family:"Roboto Condensed",sans-serif;font-weight:700;font-size:19px;color:var(--white);white-space:nowrap}
.back-cta .cta-phone{position:absolute;left:334px;top:1px;font-family:"Roboto Condensed",sans-serif;font-weight:700;font-size:27px;color:var(--white);white-space:nowrap}
.frame-right{left:807px;top:0;width:17px;height:549px;background:var(--frame)}
.frame-bottom{left:0;top:536px;width:824px;height:13px;background:var(--frame)}
.stamp{left:710px;top:25px;width:70px;height:94px;border:1px solid #555}
.addr-line{left:614px;width:170px;height:1px;background:#8a8a8a}
</style>
</head>
<body>

<!-- Front of card -->
<section class="abs front">
  <div class="abs brand"><span class="dot"></span>Harlow Safety</div>
  <div class="abs front-contact">412 Orchard Lane, Suite 5, P.O. Box 41820<br>Maple Grove, CA 94588<br>Phone : 800-555-0142, Fax : 925-555-0187</div>

  <div class="abs letter">
    <p class="salute">Dear Customer Name,</p>
    <p>Harlow Safety wants to help you amend any safety hazards that may be present on your building and be prepared to show OSHA that you are doing everything necessary to provide a safe work environment on your property. We specialize in bringing any and all buildings' exterior building maintenance equipment and fall protection systems into compliance with OSHA safety standards. The more you can learn about your buildings suspended access safety, the more prepared you can be to create a safe working environment for all who work on the facades of your buildings.</p>
    <p>As a participant in the International Facade Care Guild functions and as an attendee at Society of Building Systems Engineers committee meetings, I see the concerns for workers' safety. Unfortunately, accidents do happen, but you can feel confident in preventing accidents by taking the necessary steps towards eliminating unsafe conditions.</p>
    <p>Is your building in compliance with OSHA Safety Standards? Providing a safe work environment can be a difficult task. We offer a FREE evaluation of your exterior building maintenance (window cleaning) system. In this evaluation you will receive:</p>
    <ul>
      <li>Review of all applicable building/systems documentation, records and operating procedures</li>
      <li>Review OPOS Document for possible updates or changes to the laws</li>
      <li>Recommendations for testing of safety equipment for load sustaining ability</li>
      <li>Observe all applicable roof top work areas for access safety</li>
      <li>Observe perimeter of building at ground level for work area/access safety</li>
    </ul>
    <h3>Why spend the time and money?</h3>
    <p>California adopted a new law, found in the labor code 6432, bill name AB2774, in the GISO, Title 8, that establishes new procedures and standards for an investigation and the determination by the division of DOSH of a serious violation by an employer which causes harm or exposes an employee to the risk of harm. Building owners are usually included in the term "employers" due to the nature of "multi-site" employer. This means that building owners and mangers contract to have certain activities performed by other companies, such as window cleaning, painting, etc. and are still required to provide a safe workplace. Labor Code 6400 defines "exposing employer", "controlling employer" and "correcting employer". Therefore, building owners and managers may be looked upon as the controlling employer or the correcting employer.</p>
    <p>Show that you are committed to making your building a safer place to work. Obtain all the pertinent documentation that details a safe work environment on your building. This will in turn reduce your liability exposure.</p>
    <p>With our family name embedded in the company name, our reputation is on the line!</p>
  </div>

  <svg class="abs front-banner" viewBox="0 0 588 24" preserveAspectRatio="none" aria-hidden="true">
    <polygon points="10,0 578,0 588,24 0,24" fill="var(--red)"/>
  </svg>
  <div class="abs front-banner"><span>Reduce your liability exposure!&nbsp; Call Us Today For Your Free Evaluation!</span></div>

  <div class="abs front-photo" role="img" aria-label="Photo of a high-rise rooftop with a window-cleaning davit track and safety railings"></div>

  <div class="abs seal" style="left:697px;top:398px">
    <svg width="94" height="94" viewBox="0 0 94 94" aria-hidden="true"><circle cx="47" cy="47" r="46" fill="var(--deep-red)"/></svg>
    <div class="pct">25<small>%</small></div>
    <div class="word">Discount</div>
  </div>

  <div class="abs cta-bar">
    <svg class="abs" width="824" height="48" viewBox="0 0 824 48" aria-hidden="true">
      <polygon points="0,0 490,0 470,48 0,48" fill="var(--sky)"/>
      <polygon points="490,0 824,0 824,48 470,48" fill="var(--red)"/>
    </svg>
    <span class="cta-text">Give us a Call for your FREE evaluation!</span>
    <span class="cta-phone">(800) 555-0142</span>
  </div>
</section>

<!-- Back of card -->
<section class="abs back">
  <div class="abs back-panel"></div>
  <div class="abs audience">Property Managers and Building Engineers.</div>
  <div class="abs back-brand"><span class="dot"></span><span>Harlow<br>Safety</span></div>

  <div class="abs photo" style="left:212px;top:32px;height:114px;background:linear-gradient(135deg,#8b8b88,#c4c1ba)" role="img" aria-label="Photo of a gloved hand inspecting a metal roof anchor"></div>
  <div class="abs photo" style="left:379px;top:32px;height:114px;background:linear-gradient(135deg,#8a6a48,#b89468)" role="img" aria-label="Photo of a wooden roof deck with an opened anchor hatch"></div>

  <div class="abs photo" style="left:46px;top:162px;height:115px;background:linear-gradient(160deg,#a9b8c8,#6f7d86)" role="img" aria-label="Photo of workers on a suspended platform atop a building"></div>
  <div class="abs photo" style="left:212px;top:162px;height:115px;background:linear-gradient(160deg,#3d3a36,#8a7f70)" role="img" aria-label="Photo of a technician drilling into concrete"></div>
  <div class="abs photo" style="left:379px;top:162px;height:115px;background:linear-gradient(160deg,#9a9a96,#6c6a66)" role="img" aria-label="Photo of a rooftop davit base with railing"></div>

  <div class="abs photo" style="left:46px;top:292px;height:112px;background:linear-gradient(180deg,#b9c6d3,#8c98a0 70%,#6f7c86)" role="img" aria-label="Photo of a city skyline across the water"></div>
  <div class="abs photo" style="left:212px;top:292px;height:112px;background:linear-gradient(180deg,#c3c8ce,#7d8892)" role="img" aria-label="Aerial photo of downtown towers"></div>
  <div class="abs photo" style="left:379px;top:292px;height:112px;background:linear-gradient(180deg,#c6d2de,#8a8d88)" role="img" aria-label="Photo of a city waterfront with construction cranes"></div>

  <div class="abs seal" style="left:462px;top:354px">
    <svg width="94" height="94" viewBox="0 0 94 94" aria-hidden="true"><circle cx="47" cy="47" r="46" fill="var(--deep-red)"/></svg>
    <div class="pct">25<small>%</small></div>
    <div class="word">Discount</div>
  </div>

  <div class="abs back-address">412 Orchard Lane, Suite 5, P.O. Box 41820, Maple Grove, CA&nbsp; 94588,&nbsp; Fax:&nbsp;&nbsp; 925-555-0187</div>
  <div class="abs back-cta">
    <span class="cta-text">Give us a call for your FREE evaluation!</span>
    <span class="cta-phone">(800) 555-0142</span>
  </div>

  <div class="abs stamp"></div>
  <div class="abs addr-line" style="top:222px"></div>
  <div class="abs addr-line" style="top:252px"></div>
  <div class="abs addr-line" style="top:282px"></div>

  <div class="abs frame-right"></div>
  <div class="abs frame-bottom"></div>
</section>

</body>
</html>
```